Book Cover " FROM GRAVEL TO AMBER"

Looking for a book cover for a novel from Gravel to Amber.
Amber is the characters developed name. The book describes his rough up bringing and how he obtains his greatness and his given name Amber.

```html
<!DOCTYPE html>
<html lang="en">
<head>
<meta charset="utf-8">
<title>From Gravel to Amber — Book Cover</title>
<link rel="stylesheet" href="https://fonts.googleapis.com/css2?family=Cinzel:wght@400;500&display=swap">
<style>
  :root {
    --stage: #454545;
    --cover-top: #6e5330;
    --cover-mid: #8f6a36;
    --cover-low: #b08347;
    --cover-bottom: #b88c50;
    --gold-light: #fff2a0;
    --gold-mid: #e2bd3c;
    --gold-deep: #b8861a;
    --author-ink: #2a1d0e;
  }
  html, body {
    margin: 0;
    padding: 0;
    width: 1200px;
    height: 1200px;
    overflow: hidden;
    background: var(--stage);
  }
  .canvas {
    position: relative;
    width: 1200px;
    height: 1200px;
    display: flex;
    align-items: center;
    justify-content: center;
  }
  .book-cover {
    position: relative;
    width: 734px;
    height: 1100px;
    overflow: hidden;
    box-shadow: 0 18px 40px rgba(0,0,0,0.45);
  }
  .cover-art {
    position: absolute;
    inset: 0;
    background:
      radial-gradient(ellipse 70% 30% at 40% 78%, rgba(210,165,95,0.35), transparent 70%),
      radial-gradient(ellipse 60% 20% at 65% 62%, rgba(90,65,30,0.25), transparent 70%),
      linear-gradient(180deg, var(--cover-top) 0%, var(--cover-mid) 38%, var(--cover-low) 60%, var(--cover-bottom) 100%);
  }
  .cover-title {
    position: absolute;
    top: 340px;
    left: 0;
    right: 0;
    margin: 0;
    text-align: center;
    font-family: "Cinzel", "Trajan Pro", serif;
    font-weight: 400;
    font-size: 82px;
    line-height: 96px;
    letter-spacing: 1px;
    background: linear-gradient(180deg, var(--gold-light) 0%, var(--gold-mid) 50%, var(--gold-deep) 100%);
    -webkit-background-clip: text;
    background-clip: text;
    color: transparent;
    filter: drop-shadow(1px 2px 2px rgba(60,35,5,0.55));
  }
  .cover-title .title-line { display: block; }
  .cover-author {
    position: absolute;
    top: 900px;
    left: 0;
    right: 0;
    margin: 0;
    text-align: center;
    font-family: "Cinzel", "Trajan Pro", serif;
    font-weight: 400;
    font-size: 26px;
    letter-spacing: 10px;
    color: var(--author-ink);
  }
</style>
</head>
<body>
  <main class="canvas">
    <section class="book-cover">
      <div class="cover-art" role="img" aria-label="Photographic texture of coarse golden-brown sandpaper grain at the top fading into soft draped amber silk fabric at the bottom"></div>
      <h1 class="cover-title">
        <span class="title-line">FROM</span>
        <span class="title-line">GRAVEL</span>
        <span class="title-line">TO AMBER</span>
      </h1>
      <p class="cover-author">AUTHOR NAME</p>
    </section>
  </main>
</body>
</html>
```